New Logo and Business Card

Want new logo and business card for multi brand website. Attached are the logos for the back of the card.
We want a new logo for the front, the name "Tallvane" as the company name.
The logo can just be an "T" and a "V" for simplicity. With the text "Tallvane" after it.
For the business card use this info:
Doran Pelliske, PEng MBA
President
doran.pelliske@tallvane-mail.ca
+14035558213
Industry/Entity Type
Business
Logo Text
Tallvane
Logo styles of interest
Lettermark Logo

```html
<!DOCTYPE html>
<html lang="en">
<head>
<meta charset="utf-8">
<title>Tallvane Business Card</title>
<link href="https://fonts.googleapis.com/css2?family=Quicksand:wght@400;500&family=Oswald:wght@600&family=Open+Sans:wght@400;600&display=swap" rel="stylesheet">
<style>
  :root {
    --backdrop: #2b2a29;
    --card-dark: #3b3b3d;
    --card-dark-stripe: #4a4a4c;
    --card-light: #ffffff;
    --brand-blue: #1a86cc;
    --ink: #3c3c3c;
    --ink-soft: #7a7a7a;
    --band: #6b6b6b;
    --band-dark: #4e4e4e;
    --band-text: #ffffff;
    --logo-grey: #a9a9ab;
  }
  * { box-sizing: border-box; margin: 0; padding: 0; }
  html, body {
    width: 1200px; height: 800px; overflow: hidden;
    background: var(--backdrop);
  }
  .canvas {
    position: relative; width: 1200px; height: 800px;
    display: flex; align-items: center; justify-content: center; gap: 40px;
  }
  .card {
    position: relative; width: 540px; height: 309px;
    border-radius: 3px; overflow: hidden;
    box-shadow: 0 12px 30px rgba(0,0,0,.35);
  }

  /* Front */
  .card-front { background: var(--card-dark); }
  .front-stripes {
    position: absolute; top: 0; left: 250px; width: 150px; height: 110px;
    display: flex; flex-direction: column; gap: 6px; padding-top: 14px;
  }
  .front-stripes span {
    display: block; height: 12px; background: var(--card-dark-stripe);
  }
  .front-stripes span:nth-child(2) { opacity: .85; }
  .front-stripes span:nth-child(3) { opacity: .7; }
  .front-stripes span:nth-child(4) { opacity: .55; }
  .front-stripes span:nth-child(5) { opacity: .4; }
  .front-brand {
    position: absolute; top: 150px; left: 0; width: 100%;
    display: flex; align-items: center; justify-content: center; gap: 12px;
  }
  .brand-dot {
    width: 28px; height: 28px; border-radius: 50%; background: var(--brand-blue);
  }
  .brand-name {
    font-family: 'Quicksand', sans-serif; font-weight: 500;
    font-size: 30px; letter-spacing: 1px; color: var(--logo-grey);
  }

  /* Back */
  .card-back { background: var(--card-light); }
  .identity { position: absolute; top: 52px; left: 40px; }
  .person-name {
    font-family: 'Quicksand', sans-serif; font-weight: 500;
    font-size: 24px; color: var(--ink);
  }
  .credentials {
    font-family: 'Open Sans', sans-serif; font-size: 10px;
    color: var(--ink-soft); margin-left: 4px; letter-spacing: .5px;
  }
  .role {
    font-family: 'Oswald', sans-serif; font-weight: 600;
    font-size: 19px; color: var(--brand-blue); letter-spacing: .2px;
    line-height: 1.1; margin-top: 2px;
  }
  .contact-band {
    position: absolute; top: 112px; left: 300px; right: 0;
  }
  .contact-row {
    display: flex; align-items: center; height: 26px; background: var(--band);
    margin-bottom: 3px;
  }
  .contact-icon {
    width: 26px; height: 26px; background: var(--band-dark);
    display: flex; align-items: center; justify-content: center;
    margin-right: 10px;
  }
  .contact-text {
    font-family: 'Open Sans', sans-serif; font-size: 12px; color: var(--band-text);
  }
  .partners {
    position: absolute; left: 30px; right: 30px; bottom: 36px;
    display: flex; align-items: center; justify-content: space-between;
  }
  .partner {
    display: flex; align-items: center; gap: 6px;
    font-family: 'Quicksand', sans-serif; font-weight: 500;
    font-size: 14px; color: var(--ink-soft);
  }
  .partner-mark-circle {
    width: 16px; height: 16px; border-radius: 50%; background: var(--logo-grey);
  }
  .partner-mark-square {
    width: 14px; height: 14px; background: var(--brand-blue);
  }
</style>
</head>
<body>
<main class="canvas">
  <section class="card card-front" aria-label="Card front">
    <div class="front-stripes"><span></span><span></span><span></span><span></span><span></span></div>
    <div class="front-brand">
      <span class="brand-dot"></span>
      <span class="brand-name">tallvane</span>
    </div>
  </section>

  <section class="card card-back" aria-label="Card back">
    <div class="identity">
      <p class="person-name">Doran Pelliske,<span class="credentials">PENG MBA</span></p>
      <p class="role">PRESIDENT</p>
    </div>

    <div class="contact-band">
      <div class="contact-row">
        <span class="contact-icon">
          <svg width="14" height="14" viewBox="0 0 24 24" aria-hidden="true"><path fill="#fff" d="M6.6 10.8a15.1 15.1 0 0 0 6.6 6.6l2.2-2.2c.3-.3.7-.4 1-.2 1.1.4 2.3.6 3.6.6.6 0 1 .4 1 1V20c0 .6-.4 1-1 1A17 17 0 0 1 3 4c0-.6.4-1 1-1h3.5c.6 0 1 .4 1 1 0 1.3.2 2.5.6 3.6.1.3 0 .7-.2 1z"/></svg>
        </span>
        <span class="contact-text">+14035558213</span>
      </div>
      <div class="contact-row">
        <span class="contact-icon">
          <svg width="14" height="12" viewBox="0 0 24 18" aria-hidden="true"><rect x="1" y="1" width="22" height="16" fill="none" stroke="#fff" stroke-width="2"/><path d="M1 1l11 9 11-9" fill="none" stroke="#fff" stroke-width="2"/></svg>
        </span>
        <span class="contact-text">doran.pelliske@tallvane-mail.ca</span>
      </div>
    </div>

    <div class="partners">
      <span class="partner"><span class="partner-mark-circle"></span>Norvel Rest</span>
      <span class="partner">Quiet Cellar</span>
      <span class="partner"><span class="partner-mark-circle"></span>Greenway Fuel</span>
      <span class="partner"><span class="partner-mark-square"></span>Bright Bite</span>
    </div>
  </section>
</main>
</body>
</html>
```